Harbor Nightclub

Nightclub flyer., digital single sided, for KV and PX. I included samples of some previous flyers we've used. Sample Info:
HARBOR
FRIDAYS
FRI MAY 1 2020
DJ VORTAN (club floor)
DJ RUZO & DJ TAV (residents on the lounge floor)
4217 Marlow Avenue Sacramento
www.harborvenuehall.example for list/VIP inquiries

Target Market(s)

Upscale top 40 crowd but want some cool and artsy like the examples included.

Font styles to use
Sans Serif

Requirements
Must have
• Harbor Logo
Nice to have
• Would be nice if the flyer can be incorporated later with DJ photos (sometimes we will add dj photos to pixagram etc). Would like a big city type of feel.
Should not have
• Nothing too sexual.

```html
<!DOCTYPE html>
<html lang="en">
<head>
<meta charset="utf-8">
<title>Harbor Nightclub – Friday, May 1st</title>
<link href="https://fonts.googleapis.com/css2?family=Cabin:wght@700&family=Jost:wght@400;700&display=swap" rel="stylesheet">
<style>
  :root {
    --night: #000000;
    --deep-violet: #1c0b3d;
    --glow-violet: #4a1c8c;
    --hot-pink: #e6007e;
    --soft-pink: #ff5fbf;
    --white: #ffffff;
    --silver: #d9d9de;
    --ball-light: #fbe6f7;
    --ball-mid: #c35bb8;
    --ball-dark: #5a2584;
  }
  html, body {
    margin: 0;
    padding: 0;
    width: 995px;
    height: 1200px;
    overflow: hidden;
    background: var(--night);
  }
  .flyer {
    position: relative;
    width: 995px;
    height: 1200px;
    overflow: hidden;
    background:
      radial-gradient(ellipse 420px 360px at 600px 400px, var(--glow-violet) 0%, var(--deep-violet) 45%, rgba(0,0,0,0) 100%),
      linear-gradient(180deg, #07031a 0%, #0a0520 60%, var(--night) 100%);
    color: var(--white);
  }
  .floor-note {
    position: absolute;
    left: 42px;
    top: 46px;
    margin: 0;
    font: 700 19px/1 "Cabin", sans-serif;
  }
  .brand {
    position: absolute;
    left: 752px;
    top: 60px;
    width: 170px;
    text-align: center;
  }
  .brand-mark {
    display: block;
    width: 70px;
    height: 70px;
    margin: 0 auto 14px;
    border-radius: 50%;
    background: var(--silver);
  }
  .brand-name {
    display: block;
    font: 400 40px/1 "Jost", sans-serif;
    letter-spacing: 2px;
    color: var(--silver);
  }
  .disco-ball {
    position: absolute;
    left: 125px;
    top: 93px;
    width: 574px;
    height: 574px;
    border-radius: 50%;
    background: radial-gradient(circle at 38% 40%, var(--ball-light) 0%, #f08ad8 22%, var(--ball-mid) 52%, var(--ball-dark) 100%);
    box-shadow: 0 0 60px rgba(200, 90, 220, 0.35);
  }
  .line {
    position: absolute;
    left: 522px;
    transform: translateX(-50%);
    margin: 0;
    white-space: nowrap;
    text-align: center;
  }
  .event-date {
    top: 716px;
    font: 400 70px/1 "Jost", sans-serif;
    letter-spacing: 1px;
  }
  .event-date sup {
    font-size: 30px;
    vertical-align: 32px;
    margin-left: 4px;
  }
  .headliner {
    top: 798px;
    font: 700 113px/1 "Jost", sans-serif;
    background: linear-gradient(180deg, var(--hot-pink) 0%, var(--hot-pink) 58%, var(--soft-pink) 66%, var(--hot-pink) 100%);
    -webkit-background-clip: text;
    background-clip: text;
    color: transparent;
  }
  .residents {
    top: 940px;
    font: 700 57px/1 "Jost", sans-serif;
  }
  .residents .amp {
    color: var(--hot-pink);
  }
  .address {
    top: 1028px;
    font: 700 29px/1 "Cabin", sans-serif;
  }
  .website {
    top: 1087px;
    width: 463px;
    height: 43px;
    box-sizing: border-box;
    border: 1.5px solid var(--hot-pink);
    font: 700 28px/40px "Cabin", sans-serif;
    letter-spacing: 0.5px;
  }
  .list-note {
    top: 1146px;
    font: 700 28px/1 "Cabin", sans-serif;
  }
</style>
</head>
<body>
  <main class="flyer">
    <p class="floor-note">(Residents on the lounge floor)</p>

    <div class="brand">
      <span class="brand-mark"></span>
      <span class="brand-name">HARBOR</span>
    </div>

    <div class="disco-ball" role="img" aria-label="Illustration of a glittering pink and violet mirror disco ball with light flares"></div>

    <p class="line event-date">FRIDAY, MAY 1<sup>ST</sup></p>
    <h1 class="line headliner">DJ VORTAN</h1>
    <p class="line residents">DJ RUZO <span class="amp">&amp;</span> DJ TAV</p>
    <p class="line address">4217 Marlow Avenue Sacramento</p>
    <p class="line website">www.harborvenuehall.example</p>
    <p class="line list-note">for list/VIP Inquries</p>
  </main>
</body>
</html>
```